Email Signature

We are looking for creative email signature for our company. Please find attached the logo of our company for your reference. now we understand there isn't much can be done with email signature but we are looking for out of the box designs. Nothing specific in mind

Please insert fake numbers, website and/or address, etc just to showcase the designs. once the design is chosen we will provide the actual details.
Updates

Dear All,

We wouldlike to extend our apology for not being able to provide feedbacks to everysingle design. We were extremely busy and we have multiple contests opensimultaneously which makes the process harder. However, thank you all for theefforts you have put into this contest. We have received anoverwhelming quality responses & it has been a very difficult task tochoose just one, we easily Loved at least several designs...

Thanksagain for participating, we wish you all success in your design ventures.

Kindregards,

HLW Team

Industry/Entity Type

It Company

```html
<!DOCTYPE html>
<html lang="en">
<head>
<meta charset="utf-8">
<title>LanternWorks Email Signature</title>
<link rel="stylesheet" href="https://fonts.googleapis.com/css2?family=Lato:wght@400;900&display=swap">
<style>
  :root {
    --brand-green: #8dc63f;
    --brand-blue: #2a7fc4;
    --ink: #111111;
    --paper: #ffffff;
  }
  html, body {
    margin: 0;
    padding: 0;
    overflow: hidden;
    background: var(--paper);
  }
  .signature {
    position: relative;
    width: 1200px;
    height: 436px;
    background: var(--paper);
    font-family: "Lato", sans-serif;
    color: var(--ink);
    overflow: hidden;
  }
  .signature__rule {
    position: absolute;
    left: 35px;
    top: 35px;
    width: 1130px;
    height: 6px;
    background: linear-gradient(90deg, var(--brand-green), var(--brand-blue));
  }
  .brand-name {
    position: absolute;
    left: 62px;
    top: 66px;
    height: 330px;
    writing-mode: vertical-rl;
    transform: rotate(180deg);
    font-weight: 900;
    font-size: 54px;
    line-height: 74px;
    letter-spacing: -1px;
    color: var(--brand-blue);
    text-align: center;
    white-space: nowrap;
  }
  .contact-list {
    position: absolute;
    left: 176px;
    top: 106px;
    margin: 0;
    padding: 0;
    list-style: none;
  }
  .contact-list__item {
    display: flex;
    align-items: center;
    height: 44px;
    margin-bottom: 35px;
    font-size: 40px;
    font-weight: 400;
    white-space: nowrap;
  }
  .contact-list__icon {
    width: 42px;
    height: 42px;
    margin-right: 14px;
    flex: none;
  }
</style>
</head>
<body>
  <div class="signature">
    <div class="signature__rule"></div>

    <div class="brand-name">LanternWorks</div>

    <ul class="contact-list">
      <li class="contact-list__item">
        <svg class="contact-list__icon" viewBox="0 0 40 40" aria-hidden="true">
          <circle cx="20" cy="20" r="18.2" fill="none" stroke="#111" stroke-width="2.8"/>
          <text x="20" y="29" text-anchor="middle" font-family="Lato, sans-serif" font-weight="900" font-size="28" fill="#111">@</text>
        </svg>
        <span>office@lanternworks.com</span>
      </li>
      <li class="contact-list__item">
        <svg class="contact-list__icon" viewBox="0 0 40 40" aria-hidden="true">
          <circle cx="20" cy="20" r="18.2" fill="none" stroke="#111" stroke-width="2.8"/>
          <path d="M12 11 l4-2 l4 6 l-3 2 q2 5 6 7 l2-3 l6 4 l-2 4 q-3 2 -8 -1 q-7 -4 -10 -11 q-1 -4 1 -6z" fill="#111"/>
        </svg>
        <span>0241 735 068</span>
      </li>
      <li class="contact-list__item">
        <svg class="contact-list__icon" viewBox="0 0 40 40" aria-hidden="true">
          <circle cx="20" cy="20" r="18.2" fill="none" stroke="#111" stroke-width="2.8"/>
          <rect x="14" y="8" width="12" height="24" rx="2" fill="#111"/>
          <rect x="16" y="11" width="8" height="7" fill="#fff"/>
          <g fill="#fff">
            <rect x="16" y="20" width="2" height="2"/><rect x="19" y="20" width="2" height="2"/><rect x="22" y="20" width="2" height="2"/>
            <rect x="16" y="23" width="2" height="2"/><rect x="19" y="23" width="2" height="2"/><rect x="22" y="23" width="2" height="2"/>
            <rect x="16" y="26" width="2" height="2"/><rect x="19" y="26" width="2" height="2"/><rect x="22" y="26" width="2" height="2"/>
          </g>
        </svg>
        <span>0796 318 452</span>
      </li>
      <li class="contact-list__item">
        <svg class="contact-list__icon" viewBox="0 0 40 40" aria-hidden="true">
          <circle cx="20" cy="20" r="18.2" fill="none" stroke="#111" stroke-width="2.8"/>
          <path d="M20 33 q-9 -11 -9 -17 a9 9 0 0 1 18 0 q0 6 -9 17z" fill="#111"/>
          <circle cx="20" cy="16" r="3.5" fill="#fff"/>
        </svg>
        <span>Brookvale, 2871, Harbor Lane, QV, 518 204</span>
      </li>
    </ul>
  </div>
</body>
</html>
```